Life Coach for Lawyers Business Card Design

Elegant, original, business card design for life coaching service for associate attorneys who work in big law and struggle with stress, overwhelm, and time management. Double sided design.

Target Market(s)

Women associate attorneys who work in big law and struggle with stress, overwhelm, and time management.

Industry/Entity Type

Life Coaching

Contact Information for Business Card

Marissa Pendrell
Life Coach
518.677.3941
calmbriefcounsel.net
marissa@calmbriefcounsel.net
@calmbriefcounsel (Instagram)

Font styles to use
Other font styles liked:
• Silver South font duo. See uploaded files.

Requirements
Must have
• Icons for phone, website, email, and Instagram instead of words. Specific colors used in my logo (171B2B, 421121, FFFFFF)
Nice to have
• Foil. Embossed. Feminine design.
Should not have
• Any colors other than those used in logo. See uploaded files.

```html
<!DOCTYPE html>
<html lang="en">
<head>
<meta charset="utf-8">
<title>Calm Brief Counsel – Business Cards</title>
<link rel="stylesheet" href="https://fonts.googleapis.com/css2?family=Libre+Baskerville:wght@400;700&display=swap">
<style>
  :root {
    --backdrop: #e9d8d8;
    --wine: #421121;
    --wine-deep: #2e1219;
    --wine-press: #240d13;
    --ink: #171b2b;
    --ink-deep: #141414;
    --white: #ffffff;
    --silver: #cfcfd3;
    --silver-soft: #a9a9ae;
  }
  * { margin: 0; padding: 0; box-sizing: border-box; }
  html, body {
    width: 1200px;
    height: 734px;
    overflow: hidden;
    background: var(--backdrop);
  }
  .canvas {
    position: relative;
    width: 1200px;
    height: 734px;
    font-family: "Libre Baskerville", Georgia, serif;
  }
  .card {
    position: absolute;
    width: 540px;
    height: 310px;
    border-radius: 18px;
    box-shadow: 0 14px 30px rgba(60, 30, 40, 0.28);
    overflow: hidden;
  }

  /* Front side */
  .card--front {
    left: 90px;
    top: 60px;
    background: linear-gradient(160deg, #3a1620 0%, var(--wine-deep) 100%);
    display: flex;
    align-items: center;
    justify-content: center;
    gap: 14px;
  }
  .front-mark {
    width: 14px;
    height: 14px;
    border-radius: 50%;
    background: var(--wine-press);
  }
  .front-name {
    font-size: 22px;
    letter-spacing: 3px;
    text-transform: uppercase;
    color: var(--wine-press);
  }

  /* Back side */
  .card--back {
    left: 570px;
    top: 364px;
    background: linear-gradient(135deg, #1f1f22 0%, var(--ink-deep) 60%, #1b1b1f 100%);
    color: var(--white);
  }
  .holder {
    position: absolute;
    left: 44px;
    top: 46px;
  }
  .holder-name {
    font-size: 22px;
    font-weight: 700;
    letter-spacing: 0.3px;
  }
  .holder-role {
    margin-top: 4px;
    font-size: 12px;
    color: var(--silver);
  }
  .holder-rule {
    margin-top: 6px;
    width: 72px;
    height: 2px;
    background: var(--white);
  }
  .brand {
    position: absolute;
    right: 44px;
    top: 118px;
    display: flex;
    align-items: center;
    gap: 9px;
  }
  .brand-mark {
    width: 9px;
    height: 9px;
    border-radius: 50%;
    background: var(--silver);
  }
  .brand-name {
    font-size: 19px;
    letter-spacing: 2px;
    text-transform: uppercase;
    color: var(--silver);
  }
  .contacts {
    position: absolute;
    left: 44px;
    bottom: 34px;
    list-style: none;
    font-size: 11.5px;
    color: var(--silver);
  }
  .contacts li {
    display: flex;
    align-items: center;
    gap: 10px;
    height: 18px;
  }
  .contacts svg {
    width: 12px;
    height: 12px;
    flex: none;
  }
</style>
</head>
<body>
<main class="canvas">
  <section class="card card--front" aria-label="Card front">
    <span class="front-mark"></span>
    <span class="front-name">Calm Brief Counsel</span>
  </section>

  <section class="card card--back" aria-label="Card back">
    <div class="holder">
      <p class="holder-name">Marissa Pendrell</p>
      <p class="holder-role">Life Coach</p>
      <div class="holder-rule"></div>
    </div>

    <div class="brand">
      <span class="brand-mark"></span>
      <span class="brand-name">Calm Brief Counsel</span>
    </div>

    <ul class="contacts">
      <li>
        <svg viewBox="0 0 24 24" aria-hidden="true"><path fill="#cfcfd3" d="M6.6 10.8a15.1 15.1 0 0 0 6.6 6.6l2.2-2.2c.3-.3.7-.4 1-.2 1.1.4 2.3.6 3.6.6.6 0 1 .4 1 1V20c0 .6-.4 1-1 1C10.6 21 3 13.4 3 4c0-.6.4-1 1-1h3.5c.6 0 1 .4 1 1 0 1.3.2 2.5.6 3.6.1.3 0 .7-.2 1z"/></svg>
        <span>518.677.3941</span>
      </li>
      <li>
        <svg viewBox="0 0 24 24" aria-hidden="true"><rect x="2.5" y="5" width="19" height="14" rx="1.5" fill="none" stroke="#cfcfd3" stroke-width="2"/><path d="M3 6l9 7 9-7" fill="none" stroke="#cfcfd3" stroke-width="2"/></svg>
        <span>marissa@calmbriefcounsel.net</span>
      </li>
      <li>
        <svg viewBox="0 0 24 24" aria-hidden="true"><g fill="none" stroke="#cfcfd3" stroke-width="1.8"><circle cx="12" cy="12" r="9.5"/><ellipse cx="12" cy="12" rx="4" ry="9.5"/><path d="M2.5 12h19M4 7h16M4 17h16"/></g></svg>
        <span>www.calmbriefcounsel.net</span>
      </li>
      <li>
        <svg viewBox="0 0 24 24" aria-hidden="true"><circle cx="12" cy="12" r="9" fill="none" stroke="#cfcfd3" stroke-width="2"/></svg>
        <span>@calmbriefcounsel</span>
      </li>
    </ul>
  </section>
</main>
</body>
</html>
```